Whitepaper: 7 Keys to Achieving Success of Your RTLS Initiative

Create a graphical layout for a whitepaper that would include 7 illustrations matching each subject line. Colors aligned with Boundless Stride branding guide (attached)
Updates

Just to summarize, I would need graphics/illustrations for 7 bullet points - Key #1: Set Measurements for Success Key #2: Establish a Clear Roadmap Key #3: Don’t Use Pilots (small try out of software) Key #4: Plan for the Future, from the Start Key #5: Think about RTLS as an Initiative, not a Project Key #6: Nurture the Change Key #7: Show Successes, Early

I would expect about 2-3 illustrations per page. Format - US size 8.5x11. PDF file, but would like to have the ability to edit text if needed. Thank you for your interest. Colors don't need to match the branding. It is a healthcare whitepaper so it could be blue and green.

Project Deadline Extended
Reason: Some of you have asked for a time extension.

```html
<!DOCTYPE html>
<html lang="en">
<head>
<meta charset="utf-8">
<title>Key #7: Show Successes, Early</title>
<link href="https://fonts.googleapis.com/css2?family=Montserrat:ital,wght@0,700;1,400&family=Raleway:wght@400&display=swap" rel="stylesheet">
<style>
  :root {
    --brand-blue: #40c5e4;
    --body-grey: #5a5a5a;
    --band-green: #a2d869;
    --white: #ffffff;
  }
  * { margin: 0; padding: 0; box-sizing: border-box; }
  html, body { width: 927px; height: 1200px; overflow: hidden; background: var(--white); }
  .page { position: relative; width: 927px; height: 1200px; overflow: hidden; }

  .key-icon { position: absolute; left: 395px; top: 143px; width: 160px; height: 160px; }

  .key-title {
    position: absolute; top: 360px; left: 0; width: 927px; text-align: center;
    font-family: "Montserrat", sans-serif; font-weight: 700; font-size: 24px;
    color: var(--brand-blue);
  }

  .key-body {
    position: absolute; left: 95px; top: 416px; width: 760px;
    font-family: "Raleway", sans-serif; font-size: 17px; line-height: 32.8px;
    color: var(--body-grey); text-align: justify;
  }
  .key-body p + p { margin-top: 17px; }

  .author-band {
    position: absolute; left: 0; top: 870px; width: 927px; height: 330px;
    background: var(--band-green);
  }
  .author-heading {
    position: absolute; left: 95px; top: 58px;
    font-family: "Montserrat", sans-serif; font-weight: 700; font-size: 20.5px;
    color: var(--white);
  }
  .author-bio {
    position: absolute; left: 95px; top: 108px; width: 760px;
    font-family: "Montserrat", sans-serif; font-style: italic; font-weight: 400;
    font-size: 16.5px; line-height: 32.8px; color: var(--white); text-align: justify;
    letter-spacing: -0.3px;
  }
</style>
</head>
<body>
<main class="page">
  <svg class="key-icon" viewBox="0 0 160 160" aria-hidden="true">
    <circle cx="80" cy="80" r="80" fill="var(--brand-blue)"/>
    <g fill="none" stroke="var(--white)" stroke-width="3.5" stroke-linecap="round">
      <circle cx="80" cy="80" r="32"/>
      <line x1="80" y1="46" x2="80" y2="58"/>
      <line x1="80" y1="102" x2="80" y2="114"/>
      <line x1="46" y1="80" x2="58" y2="80"/>
      <line x1="102" y1="80" x2="114" y2="80"/>
    </g>
    <circle cx="80" cy="80" r="7" fill="var(--white)"/>
  </svg>

  <h2 class="key-title">Key #7: Show Successes, Early</h2>

  <section class="key-body">
    <p>To create excitement around RTLS initiative, you must demonstrate the value it brings to the organization. However, don’t only focus on hard dollar savings, such as avoided rentals or purchases. Ask your nurses how much time the system saves them, how much happier they are at work. And don’t wait for the fiscal year to end to report these results, share success stories often and early to increase the system adoption and create momentum for your initiative.</p>
    <p>As you can see, ensuring the success of your RTLS initiative is not an easy task. It requires executive commitment, dedicated resources, and adoption by the staff on the floor – only then you can provide the value to your patients and staff and achieve tangible ROI to your organization.</p>
  </section>

  <section class="author-band">
    <h3 class="author-heading">About Dr. Nathan Corwell</h3>
    <p class="author-bio">Dr. Corwell is a medical informaticist and emergency medicine physician. He has been part of the design, implementation, optimization and value realization process for EHR systems, principally Meridian, through 28 hospitals and hundreds of ambulatory clinics across 3 major health care systems, both academic and non-academic. He also has a significant interest and experience with leveraging Real-Time Location technologies in the healthcare environment.</p>
  </section>
</main>
</body>
</html>
```